Emerging automotive detailing business

I am starting a small automotive detailing business in hopes of becoming a well-known detailer to work on high end cars. I would like a card to reflect the high quality and time I put into my work. The name of the company is Brightwater Kerb Detailing. I feel like it represents racecars getting off the line at the drag strip as well as an innuendo of "Up the Ladder". I do minor paint correction such as clay barring, multi-step buffing and polishing, waxing, hand washes, etc. I am always striving to learn more and improve my work. My goal is to have total customer satisfaction. This is a female run business but I do not want it to be very girly. Elegant is okay! I have pictures of my personal kestrel attached, they do not need to be incorporated but if you can think of a cool way to use 1 or all of them, go for it!

Target Market(s)

Anyone that owns a vehicle. Preferably high end vehicles such as Varello, Castenvaldi and Benotti but I will also happily work on any car, truck or suv no matter what brand.

Industry/Entity Type

Automotive

Contact Information for Business Card

Brightwater Kerb Detailing
Wendy Harlowe
4157 Quimby Hollow Rd
Red Lion PA 17492
Cell phone- call/text- 717-555-6284
email- brightwaterkerb@mailvale.test
Instagram: @brightwaterkerbdetail
Facebook: friendspage.test/brightwaterkerbdetail

Requirements
Must have
• Business name, my name, address, phone number. Listing that I do minor paint correction such as clay barring, multi-step buffing and polishing, waxing, hand washes, interior cleaning, and more. (This last part was in nice to haves but I have realized that I do really want it, so I moved it to must haves.) I want something that is different and eye-catching to my customers. Some people have done this very well with cards already submitted to me, but a lot have not. I didn't mess with the "look and feel bars" much because because I am pretty open to the overall design as long as it is not your basic run of the mill design.
Nice to have
• Something car related. Maybe an appointment time/date line. I do not have a logo, but if you would like to design one and incorporate it, that would be amazing!
Should not have
• Purple and Pink colors. Boring, basic, normal card.

```html
<!DOCTYPE html>
<html lang="en">
<head>
<meta charset="utf-8">
<title>Brightwater Kerb Detailing – Business Card Colourways</title>
<link rel="stylesheet" href="https://fonts.googleapis.com/css2?family=Quicksand:wght@400;500;700&family=Montserrat:wght@600&display=swap">
<style>
  :root {
    --ink: #ffffff;
    --seam: #1a1a1a;
    --car-yellow: #e8d21a;
    --car-shade: #9b8a0c;
    --red-bg: #7a0d0d;
    --red-panel: #6a0a0a;
    --red-bar: #ff1a1a;
    --slate-bg: #3b4252;
    --slate-panel: #323847;
    --slate-bar: #5196b5;
    --brown-bg: #514137;
    --brown-panel: #45372f;
    --brown-bar: #7d4a3a;
    --green-bg: #34472f;
    --green-panel: #2c3d28;
    --green-bar: #3cc43c;
  }
  * { box-sizing: border-box; margin: 0; padding: 0; }
  html, body { width: 1200px; height: 667px; overflow: hidden; background: var(--seam); }
  .sheet {
    width: 1200px; height: 667px;
    display: grid;
    grid-template-columns: 600px 600px;
    grid-template-rows: 333px 333px;
    gap: 1px 0;
  }
  .card {
    position: relative; overflow: hidden;
    background: radial-gradient(ellipse at 20% 30%, var(--bg) 0%, var(--panel) 75%);
    color: var(--ink);
    font-family: "Quicksand", sans-serif;
  }
  .card--red { --bg: var(--red-bg); --panel: var(--red-panel); --bar: var(--red-bar); }
  .card--slate { --bg: var(--slate-bg); --panel: var(--slate-panel); --bar: var(--slate-bar); }
  .card--brown { --bg: var(--brown-bg); --panel: var(--brown-panel); --bar: var(--brown-bar); }
  .card--green { --bg: var(--green-bg); --panel: var(--green-panel); --bar: var(--green-bar); }

  .card__panel {
    position: absolute; left: 322px; top: 0; right: 0; bottom: 0;
    background: linear-gradient(90deg, rgba(0,0,0,0.35) 0%, rgba(255,255,255,0.06) 8%, rgba(255,255,255,0.02) 60%, rgba(0,0,0,0.1) 100%);
    border-top-left-radius: 40px 300px;
  }
  .business-name {
    position: absolute; left: 358px; top: 40px;
    font-weight: 700; font-size: 13px; letter-spacing: 0.6px;
    white-space: nowrap;
  }
  .services { position: absolute; left: 54px; top: 26px; }
  .services__title {
    font-family: "Montserrat", sans-serif; font-weight: 600;
    font-size: 24px; letter-spacing: 0.5px; margin-bottom: 3px;
  }
  .services__list { list-style: none; font-size: 16.5px; line-height: 16.6px; letter-spacing: 0.9px; white-space: nowrap; }
  .services__list li::before { content: "•"; margin-right: 6px; }

  .vehicle-photo {
    position: absolute; left: 0; top: 184px; width: 327px; height: 149px;
    background: radial-gradient(ellipse at 45% 55%, var(--car-yellow) 0%, #cdb813 50%, var(--car-shade) 100%);
    border-radius: 120px 150px 10px 0 / 50px 60px 0 0;
  }

  .nameplate {
    position: absolute; left: 314px; top: 77px; width: 286px; height: 54px;
    background: var(--bar); padding: 3px 0 0 44px;
    box-shadow: -4px 4px 10px rgba(0,0,0,0.4);
  }
  .nameplate__name { font-weight: 700; font-size: 25px; line-height: 26px; letter-spacing: 1px; white-space: nowrap; }
  .nameplate__role { font-weight: 500; font-size: 19px; line-height: 18px; letter-spacing: 1.5px; }

  .contact { position: absolute; left: 366px; top: 163px; right: 6px; list-style: none; }
  .contact__item { display: flex; align-items: flex-start; gap: 9px; font-weight: 700; font-size: 12px; height: 21px; letter-spacing: 0.2px; white-space: nowrap; }
  .contact__item svg { flex: none; width: 16px; height: 16px; fill: var(--ink); }
  .contact__item--phone { font-size: 19px; height: 26px; letter-spacing: 1px; }
  .contact__item--web { font-size: 9.5px; letter-spacing: -0.1px; line-height: 16px; }
  .contact__item--address { font-size: 13px; line-height: 16px; letter-spacing: 0.6px; height: auto; }
</style>
</head>
<body>
<main class="sheet">
  <section class="card card--red">
    <div class="card__panel"></div>
    <p class="business-name">Brightwater Kerb Detailing</p>
    <div class="services"><h2 class="services__title">OUR SERVICES</h2><ul class="services__list"><li>Paint Correction</li><li>Clay Barring</li><li>Multi-step Buffing</li><li>Polishing and Waxing</li><li>Hand Washes</li><li>Interior Cleaning</li><li>And more...</li></ul></div>
    <div class="vehicle-photo" role="img" aria-label="Photo of a yellow kestrel sports car with black racing stripe"></div>
    <div class="nameplate"><p class="nameplate__name">Wendy Harlowe</p><p class="nameplate__role">Owner</p></div>
    <ul class="contact">
      <li class="contact__item contact__item--phone"><svg viewBox="0 0 16 16"><path d="M4 0h8a1 1 0 0 1 1 1v14a1 1 0 0 1-1 1H4a1 1 0 0 1-1-1V1a1 1 0 0 1 1-1zm0 2v11h8V2zm3 12v1h2v-1z"/></svg>717-555-6284</li>
      <li class="contact__item"><svg viewBox="0 0 16 16"><path d="M0 2h16v12H0zm1.5 1.5v.3L8 8.5l6.5-4.7v-.3zm0 2.1v7h13v-7L8 10.3z"/></svg>brightwaterkerb@mailvale.test</li>
      <li class="contact__item"><svg viewBox="0 0 16 16"><rect x="1" y="1" width="14" height="14" rx="2"/></svg>@brightwaterkerbdetail</li>
      <li class="contact__item contact__item--web"><svg viewBox="0 0 16 16"><rect x="1" y="1" width="14" height="14" rx="2"/></svg>friendspage.test/brightwaterkerbdetail</li>
      <li class="contact__item contact__item--address"><svg viewBox="0 0 16 16"><path d="M8 0a5.5 5.5 0 0 1 5.5 5.5C13.5 10 8 16 8 16S2.5 10 2.5 5.5A5.5 5.5 0 0 1 8 0zm0 3a2.5 2.5 0 1 0 0 5 2.5 2.5 0 0 0 0-5z"/></svg><span>4157 Quimby Hollow Rd<br>Red Lion PA 17492</span></li>
    </ul>
  </section>

  <section class="card card--slate">
    <div class="card__panel"></div>
    <p class="business-name">Brightwater Kerb Detailing</p>
    <div class="services"><h2 class="services__title">OUR SERVICES</h2><ul class="services__list"><li>Paint Correction</li><li>Clay Barring</li><li>Multi-step Buffing</li><li>Polishing and Waxing</li><li>Hand Washes</li><li>Interior Cleaning</li><li>And more...</li></ul></div>
    <div class="vehicle-photo" role="img" aria-label="Photo of a yellow kestrel sports car with black racing stripe"></div>
    <div class="nameplate"><p class="nameplate__name">Wendy Harlowe</p><p class="nameplate__role">Owner</p></div>
    <ul class="contact">
      <li class="contact__item contact__item--phone"><svg viewBox="0 0 16 16"><path d="M4 0h8a1 1 0 0 1 1 1v14a1 1 0 0 1-1 1H4a1 1 0 0 1-1-1V1a1 1 0 0 1 1-1zm0 2v11h8V2zm3 12v1h2v-1z"/></svg>717-555-6284</li>
      <li class="contact__item"><svg viewBox="0 0 16 16"><path d="M0 2h16v12H0zm1.5 1.5v.3L8 8.5l6.5-4.7v-.3zm0 2.1v7h13v-7L8 10.3z"/></svg>brightwaterkerb@mailvale.test</li>
      <li class="contact__item"><svg viewBox="0 0 16 16"><rect x="1" y="1" width="14" height="14" rx="2"/></svg>@brightwaterkerbdetail</li>
      <li class="contact__item contact__item--web"><svg viewBox="0 0 16 16"><rect x="1" y="1" width="14" height="14" rx="2"/></svg>friendspage.test/brightwaterkerbdetail</li>
      <li class="contact__item contact__item--address"><svg viewBox="0 0 16 16"><path d="M8 0a5.5 5.5 0 0 1 5.5 5.5C13.5 10 8 16 8 16S2.5 10 2.5 5.5A5.5 5.5 0 0 1 8 0zm0 3a2.5 2.5 0 1 0 0 5 2.5 2.5 0 0 0 0-5z"/></svg><span>4157 Quimby Hollow Rd<br>Red Lion PA 17492</span></li>
    </ul>
  </section>

  <section class="card card--brown">
    <div class="card__panel"></div>
    <p class="business-name">Brightwater Kerb Detailing</p>
    <div class="services"><h2 class="services__title">OUR SERVICES</h2><ul class="services__list"><li>Paint Correction</li><li>Clay Barring</li><li>Multi-step Buffing</li><li>Polishing and Waxing</li><li>Hand Washes</li><li>Interior Cleaning</li><li>And more...</li></ul></div>
    <div class="vehicle-photo" role="img" aria-label="Photo of a yellow kestrel sports car with black racing stripe"></div>
    <div class="nameplate"><p class="nameplate__name">Wendy Harlowe</p><p class="nameplate__role">Owner</p></div>
    <ul class="contact">
      <li class="contact__item contact__item--phone"><svg viewBox="0 0 16 16"><path d="M4 0h8a1 1 0 0 1 1 1v14a1 1 0 0 1-1 1H4a1 1 0 0 1-1-1V1a1 1 0 0 1 1-1zm0 2v11h8V2zm3 12v1h2v-1z"/></svg>717-555-6284</li>
      <li class="contact__item"><svg viewBox="0 0 16 16"><path d="M0 2h16v12H0zm1.5 1.5v.3L8 8.5l6.5-4.7v-.3zm0 2.1v7h13v-7L8 10.3z"/></svg>brightwaterkerb@mailvale.test</li>
      <li class="contact__item"><svg viewBox="0 0 16 16"><rect x="1" y="1" width="14" height="14" rx="2"/></svg>@brightwaterkerbdetail</li>
      <li class="contact__item contact__item--web"><svg viewBox="0 0 16 16"><rect x="1" y="1" width="14" height="14" rx="2"/></svg>friendspage.test/brightwaterkerbdetail</li>
      <li class="contact__item contact__item--address"><svg viewBox="0 0 16 16"><path d="M8 0a5.5 5.5 0 0 1 5.5 5.5C13.5 10 8 16 8 16S2.5 10 2.5 5.5A5.5 5.5 0 0 1 8 0zm0 3a2.5 2.5 0 1 0 0 5 2.5 2.5 0 0 0 0-5z"/></svg><span>4157 Quimby Hollow Rd<br>Red Lion PA 17492</span></li>
    </ul>
  </section>

  <section class="card card--green">
    <div class="card__panel"></div>
    <p class="business-name">Brightwater Kerb Detailing</p>
    <div class="services"><h2 class="services__title">OUR SERVICES</h2><ul class="services__list"><li>Paint Correction</li><li>Clay Barring</li><li>Multi-step Buffing</li><li>Polishing and Waxing</li><li>Hand Washes</li><li>Interior Cleaning</li><li>And more...</li></ul></div>
    <div class="vehicle-photo" role="img" aria-label="Photo of a yellow kestrel sports car with black racing stripe"></div>
    <div class="nameplate"><p class="nameplate__name">Wendy Harlowe</p><p class="nameplate__role">Owner</p></div>
    <ul class="contact">
      <li class="contact__item contact__item--phone"><svg viewBox="0 0 16 16"><path d="M4 0h8a1 1 0 0 1 1 1v14a1 1 0 0 1-1 1H4a1 1 0 0 1-1-1V1a1 1 0 0 1 1-1zm0 2v11h8V2zm3 12v1h2v-1z"/></svg>717-555-6284</li>
      <li class="contact__item"><svg viewBox="0 0 16 16"><path d="M0 2h16v12H0zm1.5 1.5v.3L8 8.5l6.5-4.7v-.3zm0 2.1v7h13v-7L8 10.3z"/></svg>brightwaterkerb@mailvale.test</li>
      <li class="contact__item"><svg viewBox="0 0 16 16"><rect x="1" y="1" width="14" height="14" rx="2"/></svg>@brightwaterkerbdetail</li>
      <li class="contact__item contact__item--web"><svg viewBox="0 0 16 16"><rect x="1" y="1" width="14" height="14" rx="2"/></svg>friendspage.test/brightwaterkerbdetail</li>
      <li class="contact__item contact__item--address"><svg viewBox="0 0 16 16"><path d="M8 0a5.5 5.5 0 0 1 5.5 5.5C13.5 10 8 16 8 16S2.5 10 2.5 5.5A5.5 5.5 0 0 1 8 0zm0 3a2.5 2.5 0 1 0 0 5 2.5 2.5 0 0 0 0-5z"/></svg><span>4157 Quimby Hollow Rd<br>Red Lion PA 17492</span></li>
    </ul>
  </section>
</main>
</body>
</html>
```